Modernise Business Card

Our company has been operating for 10 years. With the start of the new decade we are looking to refresh our business card design. We manufacture a range of industrial product shipping to customers internationally. A copy of our current card, both sides, is attached. We are looking for a mature professional appearance.

```html
<!DOCTYPE html>
<html lang="en">
<head>
<meta charset="utf-8">
<title>Korven Business Card</title>
<link href="https://fonts.googleapis.com/css2?family=Saira:wght@400;500;700&display=swap" rel="stylesheet">
<style>
  :root {
    --backdrop: #1a1a1a;
    --card: #232323;
    --facet: #243038;
    --accent: #1db4ec;
    --ink: #f2f2f2;
    --rule: #8a8a8a;
  }
  * { margin: 0; padding: 0; box-sizing: border-box; }
  html, body {
    width: 1200px; height: 900px; overflow: hidden;
    background: var(--backdrop);
    font-family: "Saira", sans-serif;
    color: var(--ink);
  }
  .stage {
    position: relative; width: 1200px; height: 900px;
    display: flex; flex-direction: column; align-items: center;
    justify-content: center; gap: 34px;
  }
  .card {
    position: relative; width: 640px; height: 366px;
    background: var(--card); overflow: hidden;
    box-shadow: 0 8px 24px rgba(0,0,0,.45);
  }
  .card__facet { position: absolute; inset: 0; width: 100%; height: 100%; }

  /* front */
  .front__content {
    position: absolute; inset: 0;
    display: flex; flex-direction: column; align-items: center; justify-content: center;
  }
  .brand-name {
    display: flex; align-items: center; gap: 14px;
    color: var(--accent); font-weight: 700; letter-spacing: 6px;
  }
  .brand-name__mark { width: 14px; height: 14px; background: var(--accent); }
  .front .brand-name { font-size: 58px; }
  .services {
    margin-top: 18px; list-style: none; text-align: center;
    font-size: 21px; font-weight: 500; letter-spacing: 1.5px; line-height: 1.2;
    text-transform: uppercase;
  }

  /* back */
  .back__top {
    position: absolute; left: 40px; right: 30px; top: 112px;
    display: flex; align-items: center;
  }
  .back .brand-name { font-size: 46px; width: 270px; justify-content: center; }
  .divider { width: 1px; height: 140px; background: var(--rule); margin: 0 26px 0 14px; }
  .person__name { color: var(--accent); font-size: 30px; font-weight: 700; margin-bottom: 6px; }
  .contact { list-style: none; font-size: 17px; line-height: 1.45; }
  .contact li { display: flex; align-items: center; gap: 8px; }
  .contact svg { width: 16px; height: 16px; flex: none; }
  .contact__label, .contact__highlight { color: var(--accent); }
  .address {
    position: absolute; left: 0; right: 0; bottom: 58px;
    text-align: center; font-size: 18px; line-height: 1.3; font-style: normal;
  }
</style>
</head>
<body>
<main class="stage">
  <section class="card front" aria-label="Card front">
    <svg class="card__facet" viewBox="0 0 640 366" preserveAspectRatio="none" aria-hidden="true">
      <polygon points="0,0 0,366 270,366" fill="var(--facet)"/>
    </svg>
    <div class="front__content">
      <div class="brand-name"><span class="brand-name__mark"></span>KORVEN</div>
      <ul class="services">
        <li>Hydraulic Adapters</li>
        <li>Hose Fittings</li>
        <li>Quick Couplings</li>
      </ul>
    </div>
  </section>

  <section class="card back" aria-label="Card back">
    <div class="back__top">
      <div class="brand-name"><span class="brand-name__mark"></span>KORVEN</div>
      <span class="divider"></span>
      <div class="person">
        <p class="person__name">Alan Brooke</p>
        <ul class="contact">
          <li>
            <svg viewBox="0 0 16 16" fill="none" stroke="var(--accent)" stroke-width="1.3"><circle cx="8" cy="8" r="6.6"/><path d="M5.5 4.8l1.3 1.6-.8 1c.6 1.2 1.4 2 2.6 2.6l1-.8 1.6 1.3-.8 1.2c-2.8-.3-5.4-2.9-5.7-5.7z"/></svg>
            <span><span class="contact__label">Ch:</span> +86 100 5550 0147</span>
          </li>
          <li>
            <svg viewBox="0 0 16 16" fill="none" stroke="var(--accent)" stroke-width="1.3"><circle cx="8" cy="8" r="6.6"/><path d="M5.5 4.8l1.3 1.6-.8 1c.6 1.2 1.4 2 2.6 2.6l1-.8 1.6 1.3-.8 1.2c-2.8-.3-5.4-2.9-5.7-5.7z"/></svg>
            <span><span class="contact__label">Au:</span> +61 400 555 182</span>
          </li>
          <li>
            <svg viewBox="0 0 16 16" fill="none" stroke="var(--accent)" stroke-width="1.3"><rect x="1.5" y="3.5" width="13" height="9"/><path d="M1.5 3.5l6.5 5 6.5-5"/></svg>
            <span>abrooke@korvenfittings.com</span>
          </li>
          <li>
            <svg viewBox="0 0 16 16" fill="none" stroke="var(--accent)" stroke-width="1.3"><circle cx="8" cy="8" r="6.5"/><ellipse cx="8" cy="8" rx="3" ry="6.5"/><path d="M1.5 8h13M2.5 4.8h11M2.5 11.2h11"/></svg>
            <span>www.<span class="contact__highlight">korvenfittings</span>.com</span>
          </li>
        </ul>
      </div>
    </div>
    <address class="address">
      1208-3, Lin Feng Tower, 88 Harbour Road, Eastgate District<br>
      Portside 315000 China
    </address>
  </section>
</main>
</body>
</html>
```